Bully breed rescue website

I need a website for my bully breed rescue. We rescue bully breeds from up and down the east coast of the United States and train them as service dogs for people with limited mobility disabilities. I don't want a lot of white space. I want it to be modern and slick and colorful and still look professional. I want it to be different and have a lot of wow factor. I linked a copy of my logo.

Number of Pages Required

5+ page

Font styles to use
Sans Serif

Colors

Designer to choose colors to be used in the design.

Requirements
Must have
• Moving aspects. Blog and ecommerce.
• 1.) Home page
• 2.) Services- something modular
• 3.) About US
• 4.) Blog
• 5.) Application page
• 6.) Donation page
• 7.) Contact Us
Nice to have
• Large Slider of photos on home page
• vertical menu bar
Should not have
• Lots of white space. Dont want it to look like a template or any other site

```html
<!DOCTYPE html>
<html lang="en">
<head>
<meta charset="utf-8">
<title>About Us – Quillmoor Bully Haven</title>
<link rel="stylesheet" href="https://fonts.googleapis.com/css2?family=Roboto:wght@300;400;500;700&display=swap">
<style>
  :root {
    --white: #ffffff;
    --page-grey: #e9e9e9;
    --panel-grey: rgba(236, 236, 236, 0.93);
    --ink: #1d1d1d;
    --body-text: #5a5a5a;
    --paw-red: #e8202a;
    --paw-green: #4b8d17;
    --paw-yellow: #f6c51d;
    --button-yellow: #f5d23c;
    --field: rgba(255, 255, 255, 0.88);
  }
  * { box-sizing: border-box; margin: 0; padding: 0; }
  html, body { width: 1200px; height: 2639px; overflow: hidden; background: var(--white); }
  body { font-family: "Roboto", Arial, sans-serif; color: var(--ink); }
  .canvas { position: relative; width: 1200px; height: 2639px; overflow: hidden; }

  .photo { position: absolute; }
  .hero-photo {
    left: 0; top: 0; width: 1200px; height: 640px;
    background: linear-gradient(100deg, #5f8a3a 0%, #3b4a2c 14%, #1d1d1f 35%, #2a2a2a 55%, #4a4d45 75%, #6d7066 100%);
  }
  .contact-photo {
    left: 0; top: 1760px; width: 1200px; height: 879px;
    background: linear-gradient(95deg, #5c3218 0%, #b98a63 18%, #e9e1d8 30%, #6b3a1e 48%, #8a4a22 66%, #3a1c0e 82%, #c7b7a8 100%);
  }
  .mission-photo {
    left: 600px; top: 674px; width: 558px; height: 429px;
    background: linear-gradient(135deg, #3f7d1f 0%, #8a6a4a 35%, #e8e0d4 60%, #4f8f25 100%);
  }
  .vision-photo {
    left: 40px; top: 1290px; width: 560px; height: 429px;
    background: linear-gradient(130deg, #0c0c0c 0%, #1b1b1b 30%, #e8e4de 55%, #d9d2c8 70%, #5a4630 100%);
  }

  .shapes { position: absolute; left: 0; top: 0; width: 1200px; height: 2639px; }

  .brand {
    position: absolute; left: 40px; top: 78px;
    display: flex; align-items: center; gap: 10px;
    font-weight: 700; font-size: 22px; color: var(--white);
  }
  .brand-dot { width: 22px; height: 22px; border-radius: 50%; background: var(--white); }
  .menu-toggle {
    position: absolute; left: 1094px; top: 50px; width: 64px; height: 64px;
    border: 2px solid var(--ink); border-radius: 50%;
  }
  .menu-toggle span {
    position: absolute; left: 19px; width: 24px; height: 2px; background: var(--ink);
  }
  .menu-toggle span:nth-child(1) { top: 22px; }
  .menu-toggle span:nth-child(2) { top: 30px; }
  .menu-toggle span:nth-child(3) { top: 38px; }

  .page-title {
    position: absolute; left: 0; top: 290px; width: 1200px; text-align: center;
    font-size: 66px; font-weight: 700; color: var(--white); letter-spacing: -1px;
  }

  .paw { position: absolute; width: 54px; height: 54px; }
  .paw.red { fill: var(--paw-red); }
  .paw.green { fill: var(--paw-green); }
  .paw.yellow { fill: var(--paw-yellow); }

  .story { position: absolute; width: 348px; text-align: center; }
  .story h2 { font-size: 28px; font-weight: 500; line-height: 34px; margin-bottom: 26px; }
  .story p { font-size: 16.5px; font-weight: 300; line-height: 29.5px; color: var(--body-text); }
  .story p + p { margin-top: 29px; }
  .mission { left: 144px; top: 673px; }
  .vision { left: 711px; top: 1287px; }

  .contact-title {
    position: absolute; left: 0; top: 1880px; width: 1200px; text-align: center;
    font-size: 34px; font-weight: 500; color: var(--white);
  }
  .signup { position: absolute; left: 106px; top: 1983px; display: flex; gap: 26px; }
  .field {
    height: 80px; border-radius: 40px; background: var(--field);
    padding-left: 30px; display: flex; align-items: center;
    font-size: 17px; color: #444;
  }
  .field.name { width: 364px; }
  .field.email { width: 361px; }
  .submit {
    width: 210px; height: 80px; border-radius: 40px; background: var(--button-yellow);
    color: var(--white); font-weight: 700; font-size: 17px;
    display: flex; align-items: center; justify-content: center;
  }

  .info { position: absolute; top: 2330px; width: 260px; margin-left: -130px; text-align: center; }
  .info h3 { font-size: 28px; font-weight: 500; line-height: 34px; }
  .info p { font-size: 19px; line-height: 28px; color: #333; margin-top: 14px; }
  .info .paw { width: 50px; height: 50px; }
  .info .paw.yellow { left: 17px; top: -21px; }
  .info .paw.green { left: 133px; top: -62px; }
  .info .paw.red { left: 189px; top: -4px; }

  .divider {
    position: absolute; left: 40px; top: 2470px; width: 1118px; height: 2px;
    background: linear-gradient(90deg, var(--paw-red), var(--paw-yellow) 50%, var(--paw-green));
  }
  .copyright {
    position: absolute; left: 0; top: 2514px; width: 1200px; text-align: center;
    font-size: 14px; color: #444; letter-spacing: 0.5px;
  }
  .social { position: absolute; left: 505px; top: 2546px; display: flex; gap: 16px; }
  .social span { width: 36px; height: 36px; border-radius: 50%; background: var(--paw-yellow); }
</style>
</head>
<body>
<svg width="0" height="0" style="position:absolute">
  <defs>
    <symbol id="paw" viewBox="0 0 40 40">
      <ellipse cx="20" cy="27" rx="10" ry="8.5"/>
      <ellipse cx="8" cy="16" rx="4" ry="5.5" transform="rotate(-20 8 16)"/>
      <ellipse cx="16" cy="9" rx="4" ry="5.5" transform="rotate(-6 16 9)"/>
      <ellipse cx="25" cy="9" rx="4" ry="5.5" transform="rotate(8 25 9)"/>
      <ellipse cx="33" cy="16" rx="4" ry="5.5" transform="rotate(22 33 16)"/>
    </symbol>
  </defs>
</svg>

<div class="canvas">
  <div class="photo hero-photo" role="img" aria-label="Photo of a black and white bulldog puppy resting in a person's lap outdoors"></div>
  <div class="photo contact-photo" role="img" aria-label="Photo of two brown and white bulldogs lying side by side"></div>

  <svg class="shapes" viewBox="0 0 1200 2639" aria-hidden="true">
    <path fill="#ffffff" d="M0 580 C250 505 450 500 650 540 C850 580 1000 600 1200 607 L1200 1160 C1000 1140 800 1150 600 1180 C400 1210 200 1215 0 1200 Z"/>
    <path fill="#e9e9e9" d="M0 1200 C200 1215 400 1210 600 1180 C800 1150 1000 1140 1200 1160 L1200 1905 C1000 1900 850 1860 700 1820 C500 1770 300 1765 0 1795 Z"/>
    <path fill="rgba(236,236,236,0.93)" d="M0 2220 C200 2160 420 2170 650 2155 C850 2142 1000 2150 1200 2145 L1200 2639 L0 2639 Z"/>
  </svg>

  <div class="photo mission-photo" role="img" aria-label="Photo of a brindle and white bulldog panting on green grass"></div>
  <div class="photo vision-photo" role="img" aria-label="Photo of a white bulldog puppy resting on a leather cushion"></div>

  <header>
    <div class="brand"><span class="brand-dot"></span>Quillmoor Bully Haven</div>
    <div class="menu-toggle" aria-label="Menu"><span></span><span></span><span></span></div>
    <h1 class="page-title">ABOUT US</h1>
  </header>

  <svg class="paw red" style="left:207px;top:599px"><use href="#paw"/></svg>
  <svg class="paw green" style="left:154px;top:672px"><use href="#paw"/></svg>
  <svg class="paw yellow" style="left:431px;top:663px"><use href="#paw"/></svg>
  <section class="story mission">
    <h2>OUR MISSION</h2>
    <p>Lorem Ipsum is simply dummy text of the printing and typesetting industry. Lorem Ipsum has been the industry's standard dummy text ever since the 1500s, when an unknown printer took a galley of type and scrambled it to make a type specimen book.</p>
    <p>It has survived not only five centuries,Lorem Ipsum is simply dum<br>my text of the printing and typesetting industry. Lorem Ipsum has been the industry's standard dummy text ever since the 1500s, when an unknown printer took a galley of type and scrambled it to make a type specimen book. It</p>
  </section>

  <svg class="paw red" style="left:774px;top:1215px"><use href="#paw"/></svg>
  <svg class="paw green" style="left:719px;top:1286px"><use href="#paw"/></svg>
  <svg class="paw yellow" style="left:997px;top:1277px"><use href="#paw"/></svg>
  <section class="story vision">
    <h2>OUR VISION</h2>
    <p>Lorem Ipsum is simply dummy text of the printing and typesetting industry. Lorem Ipsum has been the industry's standard dummy text ever since the 1500s, when an unknown printer took a galley of type and scrambled it to make a type specimen book.</p>
    <p>It has survived not only five centuries,Lorem Ipsum is simply dum<br>my text of the printing and typesetting industry. Lorem Ipsum has been the industry's standard dummy text ever since the 1500s, when an unknown printer took a galley of type and scrambled it to make a type specimen book. It</p>
  </section>

  <section class="contact">
    <h2 class="contact-title">GET IN TOUCH</h2>
    <div class="signup">
      <div class="field name">Your name</div>
      <div class="field email">Your email</div>
      <div class="submit">SUBMIT</div>
    </div>
  </section>

  <footer>
    <div class="info" style="left:180px">
      <svg class="paw yellow"><use href="#paw"/></svg>
      <svg class="paw green"><use href="#paw"/></svg>
      <svg class="paw red"><use href="#paw"/></svg>
      <h3>MAIL</h3>
      <p>PO Box 274<br>Harbor View WA 6104</p>
    </div>
    <div class="info" style="left:461px">
      <svg class="paw yellow"><use href="#paw"/></svg>
      <svg class="paw green"><use href="#paw"/></svg>
      <svg class="paw red"><use href="#paw"/></svg>
      <h3>HOURS</h3>
      <p>Weekdays:<br>10am - 4pm WST</p>
    </div>
    <div class="info" style="left:745px">
      <svg class="paw yellow"><use href="#paw"/></svg>
      <svg class="paw green"><use href="#paw"/></svg>
      <svg class="paw red"><use href="#paw"/></svg>
      <h3>PHONE</h3>
      <p>0400 218 736</p>
    </div>
    <div class="info" style="left:1027px">
      <svg class="paw yellow"><use href="#paw"/></svg>
      <svg class="paw green"><use href="#paw"/></svg>
      <svg class="paw red"><use href="#paw"/></svg>
      <h3>EMAIL</h3>
      <p>hello@quillmoorhaven.org</p>
    </div>

    <div class="divider"></div>
    <p class="copyright">© 2018 | QUILLMOOR BULLY HAVEN</p>
    <div class="social" aria-label="Social links"><span></span><span></span><span></span><span></span></div>
  </footer>
</div>
</body>
</html>
```